New Business Card Design Project

Harbor of the Willow Wellness Clinic PLLC
Harborofthewillowwc.example
Board Certified Nursing Coach in life, health, & wellness.
Hypnotherapy, weight loss & vitamin supplement injections, IV hydration.
Offering mobile clinics

```html
<!DOCTYPE html>
<html lang="en">
<head>
<meta charset="utf-8">
<title>Harbor of the Willow Wellness Clinic – Business Card</title>
<link href="https://fonts.googleapis.com/css2?family=Crimson+Text:wght@600&family=Lato:wght@400&family=Marcellus&display=swap" rel="stylesheet">
<style>
  :root {
    --page: #4a4a4a;
    --front-top: #4a3526;
    --front-bottom: #2f2219;
    --back: #5a4332;
    --orange: #e8781f;
    --gold: #f1a33a;
    --cream: #f4ece2;
    --line: rgba(232, 120, 31, 0.75);
  }
  * { box-sizing: border-box; margin: 0; padding: 0; }
  html, body { width: 1200px; height: 900px; overflow: hidden; background: var(--page); }
  .canvas { position: relative; width: 1200px; height: 900px; }

  .card {
    position: absolute;
    left: 250px;
    width: 700px;
    height: 400px;
    border-radius: 34px;
    box-shadow: 0 14px 30px rgba(0,0,0,0.45);
    overflow: hidden;
  }

  /* Front */
  .card--front {
    top: 35px;
    background: radial-gradient(ellipse at 50% 35%, var(--front-top), var(--front-bottom) 80%);
    text-align: center;
  }
  .brand-mark {
    position: absolute;
    top: 62px; left: 0; right: 0;
    display: flex; align-items: center; justify-content: center; gap: 14px;
  }
  .brand-mark__dot {
    width: 34px; height: 34px; border-radius: 50%;
    background: var(--orange);
  }
  .brand-mark__name {
    font-family: "Marcellus", serif;
    font-size: 26px;
    letter-spacing: 3px;
    color: var(--gold);
    line-height: 1.2;
    text-align: left;
  }
  .services-title {
    position: absolute;
    top: 196px; left: 0; right: 0;
    display: flex; align-items: center; justify-content: center; gap: 14px;
    font-family: "Marcellus", serif;
    font-size: 26px;
    color: var(--orange);
    letter-spacing: 1px;
  }
  .services-title::before, .services-title::after {
    content: ""; width: 140px; height: 1.5px;
    background: linear-gradient(90deg, transparent, var(--line));
  }
  .services-title::after { background: linear-gradient(90deg, var(--line), transparent); }
  .services-list {
    position: absolute;
    top: 250px; left: 20px; right: 20px;
    list-style: none;
    font-family: "Crimson Text", serif;
    font-weight: 600;
    font-size: 21px;
    line-height: 1.4;
    color: var(--cream);
  }

  /* Back */
  .card--back { top: 465px; background: var(--back); }
  .back-brand {
    position: absolute;
    left: 70px; top: 170px;
    display: flex; align-items: center; gap: 12px;
  }
  .back-brand .brand-mark__dot { width: 30px; height: 30px; }
  .back-brand .brand-mark__name { font-size: 21px; color: var(--cream); letter-spacing: 2px; }
  .back-brand__rule {
    position: absolute; left: 70px; top: 258px;
    width: 250px; height: 1px; background: var(--line);
  }
  .person {
    position: absolute;
    right: 330px; top: 270px;
    text-align: right;
    font-family: "Lato", sans-serif;
  }
  .person__role { font-size: 18px; color: var(--cream); }
  .person__name {
    font-family: "Marcellus", serif;
    font-size: 24px; color: var(--gold); letter-spacing: 1px;
  }
  .divider {
    position: absolute; left: 390px; top: 210px;
    width: 1px; height: 130px; background: var(--line);
  }
  .contact {
    position: absolute; left: 408px; top: 212px;
    list-style: none;
    font-family: "Lato", sans-serif;
    font-size: 15.5px;
    color: var(--cream);
  }
  .contact li { display: flex; align-items: center; gap: 10px; height: 32px; }
  .contact svg { width: 16px; height: 16px; flex: none; fill: var(--gold); }
</style>
</head>
<body>
<main class="canvas">

  <section class="card card--front" aria-label="Card front">
    <div class="brand-mark">
      <span class="brand-mark__dot"></span>
      <span class="brand-mark__name">HARBOR OF THE WILLOW<br>WELLNESS CLINIC</span>
    </div>
    <h2 class="services-title">OUR SERVICES</h2>
    <ul class="services-list">
      <li>Board Certified Nursing Coach in life, health, &amp; wellness.</li>
      <li>Hypnotherapy, weight loss &amp; vitamin supplement injections, IV hydration.</li>
      <li>Offering mobile clinics</li>
    </ul>
  </section>

  <section class="card card--back" aria-label="Card back">
    <div class="back-brand">
      <span class="brand-mark__dot"></span>
      <span class="brand-mark__name">HARBOR OF THE WILLOW<br>WELLNESS CLINIC</span>
    </div>
    <div class="back-brand__rule"></div>

    <div class="person">
      <p class="person__role">Founder</p>
      <p class="person__name">JOHN SMITH</p>
    </div>

    <div class="divider"></div>

    <ul class="contact">
      <li>
        <svg viewBox="0 0 24 24"><path d="M6.6 10.8a15 15 0 0 0 6.6 6.6l2.2-2.2c.3-.3.7-.4 1-.2 1.1.4 2.3.6 3.6.6.6 0 1 .4 1 1V20c0 .6-.4 1-1 1A17 17 0 0 1 3 4c0-.6.4-1 1-1h3.5c.6 0 1 .4 1 1 0 1.3.2 2.5.6 3.6.1.3 0 .7-.2 1z"/></svg>
        555-200-9000
      </li>
      <li>
        <svg viewBox="0 0 24 24"><path d="M2 5h20v14H2z" fill="none" stroke="currentColor"/><path d="M2 5h20v14H2V5zm2 2v.3l8 5.2 8-5.2V7H4z"/></svg>
        info@harborofthewillowwc.example
      </li>
      <li>
        <svg viewBox="0 0 24 24"><path d="M12 2a10 10 0 1 0 0 20 10 10 0 0 0 0-20zm6.9 6h-3a15 15 0 0 0-1.3-4A8 8 0 0 1 18.9 8zM12 4c.8 1.2 1.5 2.5 1.9 4h-3.8c.4-1.5 1.1-2.8 1.9-4zM4.3 14a8 8 0 0 1 0-4h3.4a16 16 0 0 0 0 4zm.8 2h3a15 15 0 0 0 1.3 4A8 8 0 0 1 5.1 16zm3-8h-3a8 8 0 0 1 4.3-4c-.6 1.2-1 2.6-1.3 4zM12 20c-.8-1.2-1.5-2.5-1.9-4h3.8c-.4 1.5-1.1 2.8-1.9 4zm2.3-6H9.7a14 14 0 0 1 0-4h4.6a14 14 0 0 1 0 4zm.3 6c.6-1.2 1-2.6 1.3-4h3a8 8 0 0 1-4.3 4zm1.7-6a16 16 0 0 0 0-4h3.4a8 8 0 0 1 0 4z"/></svg>
        www.harborofthewillowwc.example
      </li>
      <li>
        <svg viewBox="0 0 24 24"><path d="M12 2a7 7 0 0 0-7 7c0 5.2 7 13 7 13s7-7.8 7-13a7 7 0 0 0-7-7zm0 9.5a2.5 2.5 0 1 1 0-5 2.5 2.5 0 0 1 0 5z"/></svg>
        00 dummy city, dummy place 0000
      </li>
    </ul>
  </section>

</main>
</body>
</html>
```